Create Premium Wine Label Design

We are premium wine exporters from Australia. We are looking to introduce new brand " The Velloro" - in red wine, White wine and Sparkling wine to international market.

The sample label design for red wine ( Shiraz) is attached.

This is our luxury brand. We need a stunning wine label designs for (front, back and neck) that should be mostly in GOLD colour and design should be really eye catching.

We have provided sample design for front, back and neck labels. However, we are looking forward to see a completely new improvised design.

LOGO attached.

Front Label Design Specification:

* We would like to see designs that are in Gold colour.
* Wine Bottle size is standard: 750ml; we assume the same design can be resizable to different bottle sizes.
* Our design should suit both black, white and sparkling wine bottles(sample attached)
* Use our logo in the design (see attached - label sample)
* Content for front label (see attached).
* Design should include all information specified in the sample

Back Label Design
* All contents in the sample should be used ( sample attached)
* LOGO attached.

Neck Label Design
* Sample of Neck label attached, please provide similar or your own design.
* LOGO attached.

Image Samples:
* Samples of label designs we like (see attached)
* Sample for gold color (see attached)
* For bottle shapes (see attached)
* Front, Back and Neck Label Samples (see attached)

Target Market(s)

International Wine Market

Font styles to use
Decorative
Script

Requirements
Must have
• Must have golden color on front and back label

```html
<!DOCTYPE html>
<html lang="en">
<head>
<meta charset="utf-8">
<title>The Velloro – Shiraz Labels</title>
<link href="https://fonts.googleapis.com/css2?family=Cinzel:wght@600&family=Lobster+Two&family=Playball&family=PT+Sans:wght@400;700&display=swap" rel="stylesheet">
<style>
  :root {
    --bg: #e9e7e2;
    --gold-light: #f6dc8a;
    --gold: #d4a83a;
    --gold-deep: #9c7320;
    --cream: #f3e2ad;
    --cream-deep: #e6cc84;
    --navy: #1f2a33;
    --wine: #a3242e;
    --ink: #2b2418;
    --white: #ffffff;
  }
  * { box-sizing: border-box; margin: 0; padding: 0; }
  html, body { width: 1200px; height: 960px; overflow: hidden; }
  body { background: var(--bg); font-family: "PT Sans", sans-serif; color: var(--ink); position: relative; }

  .front-label { position: absolute; left: 140px; top: 90px; width: 460px; height: 760px; }
  .front-label .label-shape { position: absolute; inset: 0; }
  .label-body { position: absolute; inset: 0; text-align: center; }

  .brand-mark { position: absolute; top: 120px; left: 0; right: 0; display: flex; align-items: center; justify-content: center; gap: 12px; }
  .brand-dot { width: 22px; height: 22px; border-radius: 50%; background: var(--navy); }
  .brand-name { font-family: "Cinzel", serif; font-weight: 600; font-size: 26px; letter-spacing: 3px; color: var(--navy); }

  .varietal { position: absolute; top: 200px; left: 0; right: 0; font-family: "Lobster Two", cursive; font-size: 62px; color: var(--wine); line-height: 1; }
  .varietal-rule { position: absolute; top: 238px; width: 80px; height: 2px; background: var(--gold-deep); }
  .varietal-rule.left { left: 52px; }
  .varietal-rule.right { right: 52px; }
  .wine-name { position: absolute; top: 282px; left: 0; right: 0; font-family: "Playball", cursive; font-size: 30px; color: var(--ink); }
  .divider { position: absolute; top: 332px; left: 40px; right: 40px; height: 2px; background: var(--navy); }

  .tasting-note { position: absolute; top: 346px; left: 44px; right: 44px; font-size: 11.5px; line-height: 1.95; color: var(--ink); }

  .info-block { position: absolute; top: 492px; left: 50px; right: 50px; height: 116px; }
  .info-text { position: absolute; left: 40px; right: 90px; top: 4px; font-size: 13px; line-height: 1.5; }
  .info-text .origin { font-weight: 700; font-size: 14px; }
  .volume-box { position: absolute; right: 0; top: 0; width: 72px; height: 110px; background: var(--white); text-align: center; font-size: 11px; padding-top: 8px; line-height: 1.5; }
  .volume-box svg { margin-top: 6px; }

  .maker-band { position: absolute; left: 34px; right: 34px; top: 622px; height: 80px; background: var(--navy); color: var(--white); border-top: 3px solid var(--gold); border-bottom: 3px solid var(--gold); padding-top: 12px; }
  .maker-name { font-size: 20px; font-weight: 700; }
  .maker-place { font-size: 13px; margin-top: 4px; }

  .neck-label { position: absolute; left: 680px; top: 150px; width: 400px; height: 150px; }
  .neck-band { position: absolute; left: 0; right: 0; top: 0; height: 96px; background: var(--navy); border-top: 6px solid var(--gold); border-bottom: 6px solid var(--gold); display: flex; align-items: center; justify-content: center; }
  .neck-name { font-family: "Cinzel", serif; font-weight: 600; font-size: 40px; letter-spacing: 3px; color: var(--gold-light); }
  .neck-flourish { position: absolute; left: 110px; right: 110px; top: 104px; height: 26px; border-radius: 13px; background: linear-gradient(90deg, var(--gold-deep), var(--gold-light), var(--gold-deep)); }
</style>
</head>
<body>

<section class="front-label">
  <svg class="label-shape" viewBox="0 0 460 760" width="460" height="760">
    <defs>
      <linearGradient id="goldFrame" x1="0" y1="0" x2="1" y2="1">
        <stop offset="0" stop-color="#f6dc8a"/>
        <stop offset="0.5" stop-color="#b88a2a"/>
        <stop offset="1" stop-color="#f1d37a"/>
      </linearGradient>
      <radialGradient id="creamField" cx="0.5" cy="0.35" r="0.8">
        <stop offset="0" stop-color="#f6e7b8"/>
        <stop offset="1" stop-color="#e2c77f"/>
      </radialGradient>
    </defs>
    <path d="M12,140 L12,84 Q44,84 44,52 L104,52 Q156,52 186,10 L274,10 Q304,52 356,52 L416,52 Q416,84 448,84 L448,706 Q448,750 404,750 L56,750 Q12,750 12,706 Z" fill="url(#goldFrame)"/>
    <path role="img" aria-label="Cream label ground with a faint vine and grape pattern" d="M22,142 L22,94 Q54,92 54,62 L106,62 Q160,62 192,20 L268,20 Q300,62 354,62 L406,62 Q406,92 438,94 L438,704 Q438,740 402,740 L58,740 Q22,740 22,704 Z" fill="url(#creamField)"/>
  </svg>

  <div class="label-body">
    <div class="brand-mark"><span class="brand-dot"></span><span class="brand-name">SOUTHVALE</span></div>
    <span class="varietal-rule left"></span><span class="varietal-rule right"></span>
    <div class="varietal">shiraz</div>
    <div class="wine-name">The Velloro</div>
    <div class="divider"></div>
    <p class="tasting-note">Southvale The Velloro is a Classic fruit driven wine bursting with aromas of dark fruits and spice with background notes of charred French oak. This is a full bodied wine showcasing rich and juicy dark fruits of plum and cherry balanced with soft tannins and oak, providing a long lasting finish. This wine matches perfectly with range of rich and hearty red meat or pasta dishes.</p>

    <div class="info-block">
      <div class="info-text">
        <div class="origin">Product of Australia</div>
        <div>Preservative (220)</div>
        <div>Antioxident (300).</div>
        <div>May Contain Traces of Milk.</div>
        <div>Country of Origin : Australia</div>
      </div>
      <div class="volume-box">
        <div>750 mL</div>
        <div>12.5% Alc</div>
        <svg width="22" height="38" viewBox="0 0 22 38" aria-hidden="true">
          <path d="M3,2 L19,2 Q20,16 11,20 Q2,16 3,2 Z" fill="none" stroke="#2b2418" stroke-width="2"/>
          <path d="M4,9 L18,9 Q17,17 11,19 Q5,17 4,9 Z" fill="#2b2418"/>
          <line x1="11" y1="20" x2="11" y2="33" stroke="#2b2418" stroke-width="2"/>
          <line x1="5" y1="34" x2="17" y2="34" stroke="#2b2418" stroke-width="2"/>
        </svg>
      </div>
    </div>

    <div class="maker-band">
      <div class="maker-name">Southvale Wines Pty. Ltd.,</div>
      <div class="maker-place">Ashford Vale, Victoria, Australia</div>
    </div>
  </div>
</section>

<section class="neck-label">
  <div class="neck-band"><span class="neck-name">SOUTHVALE</span></div>
  <div class="neck-flourish" role="img" aria-label="Gold ornamental flourish under the neck band"></div>
</section>

</body>
</html>
```